Website - TRSC

Having reviewed the designs received so far, no one design is meeting the client’s needs. The client has identified desirable elements from the designs submitted, which we want to see brought together.
Header
It is important that the logo is given space – ie is not overlayed on an image, nor with a short fade into an image. A gradual fade into the header image is acceptable.
Background
While an image background is acceptable, this should only be visible on the left and right borders, it should not be used underneath the main content area.
Main menu
The main menu should be a cohesive bar across the page – not separate buttons. Buttons that are connected together within a bar are acceptable. Menu items should be separated using a pipe ( | ), or by being framed (as long as the framing sits within a bar). Menu item should change colour to indicate the page you are on.
Left Hand Boxes
There should be consistency in colouring through these. It is acceptable to use one colour for the heading , and another for the content area. It is not acceptable for each box to have a different scheme. This applies to the right hand feature boxes as well.
Colouring
We want to keep this simple. Please use colours from the logo, feel free to add complimentary colours but keep the palette limited. If shading is used with any of the colours be careful to not move it too far from the original colour. The yellow does not look good with too much of a grey shade.
Feature Boxes
The two feature boxes on the home page (Browse Homes and Local Knowledge) need to stand out. An option is to ensure that the associated link button uses one of the brighter colours in the palette.
_____________________________________________________
Note: I have attached the newly design logo to the brief. It is important that colours from the logo are used on the design. Blue denotes water and the yellow denotes sand and sun.
I'd like to see the feel of the logo reflected in the site.
______________________________________________
Tui Crib and Seaside Cottages is rebuilding its website – www.tuicribandseasidecottages.co.nz.
We require the design of two pages:
• Home
• House detail page (pgs 3-5 of the attachment).
We have specified a layout for the site (attached).
The contextual information below provides the feeling the site needs to convey.
If further information is required please contact us.
CONTEXT/BACKGROUND
Tui Crib and Seaside Cottages (TRSC) has been in business now for over 11 years and is due for a facelift. We have about 40 – 60 houses available during the peak summer period – about 50% are permanent holiday homes, the balance are local family homes being rented out while they are away on holiday.
We are currently located in Marram Sands – but with the national name have the ability and goal to expand into other areas of New Zealand – so any logo etc has to have the ability to represent other holiday destinations within NZ. Bear in mind that our primary location is Marram at the moment.
Our key market is families going on holiday – looking for a holiday home to book (currently an Marram Sands holiday)
Secondary market is couples or mature groups looking at having some R&R or business groups having some team building/ management meetings away from the busy office surroundings.
We manage ALL the properties so are a great source of information on what holiday home is best suited to each family and “things to do” in the area – i.e. other activities.
Our main focus is to be the best “holiday home” - accommodation provider in whatever location TRSC is representing. We want to be seen as having a good supply of great homes, providing a great service as well as being a good source of local knowledge.
We want to be seen as PROFESSIONALS in the holiday rental business (from occupants and owners).
TRUST – we want people to be able to trust us by listing their property with us (owners) and confidently booking accommodation through us (occupants).
TAGLINE SUGGESTIONS
Key motif – “TRSC, your door to a fine escape!” The “key”, of course is a double play on the house key you get. But it is also extendible to other aspect of the experience we offer. For example the phrase: “getting the key to the city” is applicable to us – we give them the key to Marram…(or whatever location we are marketing in the future). Potentially we may consider promotional merchandise around this, eg promo key rings etc.
Some key words/phrases that our business represents are:
• ‘Our place is your place’
• Connect – connecting families to holiday homes and the area – at the moment only Marram.
• Local – local people looking after your needs – “our place is your place – so make yourself at home!”
• Link – we are the link to a real kiwi holiday experience.
• Holiday - R&R – rest and recreation
More specific to Marram:
• Safe Natural playground – beach, bush, fishing, outdoor activities – creating real family memories.
Website:
• Need to focus on the Local and Personal property management factors in website to differentiate us from other nationwide listing sites – contact us and we can help you find the right accommodation and save you time
• Play on the HOLIDAYMAKER experience more, including giving prominence to visitor deals, become a local etc, differentiating us from other local holiday home rental businesses.
• Real – real people, real places, real experiences.
• User friendly, informative, professional with a personal touch/feel, to encourage the holiday feeling.
Having reviewed the designs received so far, no one design is meetingthe client’s needs. The client has identified desirable elements from thedesigns submitted, which we want to see brought together.
Header
It is important that the logo is given space – ie is not overlayed on animage, nor with a short fade into an image. A gradual fade into the headerimage is acceptable.
Background
While an image background is acceptable, this should only be visible onthe left and right borders, it should not be used underneath the main contentarea.
Main menu
The main menu should be a cohesive bar across the page – not separatebuttons. Buttons that are connected together within a bar are acceptable.Menu items should be separated using a pipe ( | ), or by being framed (as longas the framing sits within a bar). Menu item should change colour to indicatethe page you are on.
Left Hand Boxes
There should be consistency in colouring through these. It isacceptable to use one colour for the heading , and another for the contentarea. It is not acceptable for each box to have a different scheme. Thisapplies to the right hand feature boxes as well.
Colouring
We want to keep this simple. Please use colours from the logo,feel free to add complimentary colours but keep the palette limited. Ifshading is used with any of the colours be careful to not move it too far fromthe original colour. The yellow does not look good with too much of agrey shade.
Feature Boxes
The two feature boxes on the home page (Browse Homes and LocalKnowledge) need to stand out. An option is to ensure that the associated linkbutton uses one of the brighter colours in the palette.

```html
<!DOCTYPE html>
<html lang="en">
<head>
<meta charset="utf-8">
<title>Tui Crib &amp; Seaside Cottages – Home</title>
<link href="https://fonts.googleapis.com/css2?family=Varela+Round&family=Josefin+Sans:wght@600;700&family=Nunito+Sans:wght@400;700&display=swap" rel="stylesheet">
<style>
:root{
  --gold:#f2b705;
  --gold-light:#ffd21f;
  --gold-deep:#d99a00;
  --ink:#1e1e1e;
  --dark:#262626;
  --charcoal:#333;
  --paper:#fff;
  --mist:#ececec;
  --text:#555;
  --blue:#1a9be0;
  --blue-deep:#0c74b8;
  --sea:#3a8fd0;
}
*{box-sizing:border-box;margin:0;padding:0}
html,body{width:1056px;height:1200px;overflow:hidden}
body{position:relative;background:var(--paper);font-family:"Nunito Sans",Verdana,sans-serif;color:var(--text);font-size:10px}
.abs{position:absolute}
.round{font-family:"Varela Round",Arial,sans-serif}

/* header */
.header{left:0;top:0;width:1056px;height:262px;background:repeating-linear-gradient(90deg,#1b1b1b 0 3px,#222 3px 7px,#1d1d1d 7px 11px)}
.brand-panel{left:70px;top:0;width:303px;height:262px;background:linear-gradient(#f4f4f4,#e6e6e6)}
.brand-panel .cap{position:absolute;left:0;top:0;width:303px;height:13px;background:var(--gold)}
.brand-panel svg{position:absolute;left:100px;top:12px}
.brand-mark{position:absolute;left:0;width:303px;top:160px;text-align:center;font-family:"Varela Round",Arial,sans-serif;font-size:21px;color:#444;display:flex;justify-content:center;align-items:center;gap:8px}
.brand-mark .dot{width:14px;height:14px;border-radius:50%;background:var(--gold)}
.slider{left:468px;top:15px;width:477px;height:232px;background:#555;border-radius:10px}
.slider-tabs{left:420px;top:90px;width:52px;height:96px;background:#555;border-radius:8px 0 0 8px}
.slider-tabs i{position:absolute;left:17px;width:15px;height:15px;border-radius:50%;background:#1b1b1b}
.slide{left:479px;top:29px;width:451px;height:204px;border:2px solid #fff;background:linear-gradient(#2e7fd6 0,#8bc0ea 38%,#e8e2d2 55%,#3b86c4 72%,#40586d 100%)}

/* menu */
.menu{left:0;top:262px;width:1056px;height:44px;background:linear-gradient(#ffd52a,var(--gold) 60%,var(--gold-deep))}
.menu-shadow{left:0;top:306px;width:1056px;height:9px;background:linear-gradient(#bfbfbf,#fff)}
.menu ul{list-style:none;display:flex;position:absolute;left:58px;top:0;height:44px}
.menu li{font:700 11.5px "Nunito Sans",Arial,sans-serif;color:#7a5a00;height:44px;display:flex;align-items:center;justify-content:center;position:relative}
.menu li+li::before{content:"";position:absolute;left:0;top:16px;height:18px;border-left:1px solid #a47a00}
.menu li.active{background:linear-gradient(#fff,#e9e9e9);color:#222;border-radius:8px 8px 0 0;margin-top:6px;height:38px}

/* side boxes */
.side{left:67px;width:230px;border-radius:7px;background:var(--gold);border:1px solid #e2a800;overflow:hidden}
.side h3{height:36px;background:linear-gradient(#ffd429,var(--gold-deep));text-align:center;font:400 19px/36px "Varela Round",Arial,sans-serif;color:#fff;border-bottom:1px solid #b98400}
.side h3 b{font-weight:400;color:#3a2a00}
.side label{display:block;font-size:10px;color:#222}
.field{background:#fff;height:18px;border:1px solid #ddd}
.light{background:var(--paper)}
.light .body{background:linear-gradient(#fff,#e8e8e8)}

/* main */
.intro p{font-size:10.3px;line-height:18px;color:#666}
.intro p.lead{color:var(--gold-deep);font-weight:700}
.intro span{color:#666;font-weight:400}
.banner{left:330px;top:604px;width:648px;height:66px;border-radius:30px;background:linear-gradient(#454545,#141414);box-shadow:2px 3px 4px #aaa;text-align:center;font:700 19.5px/21px "Josefin Sans",Arial,sans-serif;letter-spacing:1.6px;color:#fff;padding-top:10px}
.banner em{font-style:normal;color:var(--gold)}
.feature{top:695px;width:300px;height:247px;padding:6px 6px}
.feature .photo{width:287px;height:175px;border:1px solid #fff}
.feature h4{font:400 22px "Varela Round",Arial,sans-serif;margin:3px 0 0 6px}
.feature p{font-size:10px;line-height:16px;margin-left:8px;width:250px}
.footer{left:0;top:970px;width:1056px;height:230px;background:linear-gradient(#2a2a2a,#1c1c1c)}
.footer h5{font:400 20px "Varela Round",Arial,sans-serif;color:#fff}
.footer .soft{color:#666}
.social i{position:absolute;top:5px;width:36px;height:36px;border-radius:50%}
.fnav{display:flex;gap:0;font-size:10px;color:#aaa}
.fnav span{padding:0 17px;border-left:1px solid #888}
.fnav span:first-child{border:none}
</style>
</head>
<body>

<div class="abs header"></div>
<div class="abs brand-panel">
  <div class="cap"></div>
  <svg width="104" height="60" viewBox="0 0 104 60"><polygon points="0,0 104,0 52,58" fill="#f2b705"/></svg>
  <div class="brand-mark"><span class="dot"></span>Tui Crib &amp; Seaside Cottages</div>
</div>
<div class="abs slider-tabs"><i style="top:8px"></i><i style="top:41px;background:var(--gold)"></i><i style="top:74px"></i></div>
<div class="abs slider"></div>
<div class="abs slide" role="img" aria-label="Photo of a white holiday home with a lit swimming pool at dusk"></div>

<nav class="abs menu">
  <ul>
    <li class="active" style="width:130px">HOME</li>
    <li style="width:116px">ABOUT US</li>
    <li style="width:150px">LIST YOUR HOME</li>
    <li style="width:165px">LOCALKNOWLEDGE</li>
    <li style="width:160px">BROWSE HOMES</li>
    <li style="width:130px">PACKAGES</li>
    <li style="width:125px">CONTACT US</li>
  </ul>
</nav>
<div class="abs menu-shadow"></div>

<!-- quick search -->
<section class="abs side" style="top:331px;height:210px">
  <h3>Quick <b>Search</b></h3>
  <div style="position:relative;height:172px">
    <label class="abs" style="left:18px;top:10px">No. Of Guests</label>
    <div class="abs field" style="left:10px;top:30px;width:155px;border-radius:8px"></div>
    <label class="abs" style="left:16px;top:58px">Nightly Rate</label>
    <div class="abs field" style="left:12px;top:77px;width:84px"></div>
    <label class="abs" style="left:103px;top:79px">to</label>
    <div class="abs field" style="left:122px;top:77px;width:85px"></div>
    <label class="abs" style="left:16px;top:102px">Keywords</label>
    <div class="abs field" style="left:12px;top:120px;width:152px"></div>
    <svg class="abs" style="left:175px;top:119px" width="19" height="19" viewBox="0 0 19 19"><rect width="19" height="19" rx="3" fill="#222"/><circle cx="8" cy="8" r="4" fill="none" stroke="#f2b705" stroke-width="2"/><line x1="11" y1="11" x2="15" y2="15" stroke="#f2b705" stroke-width="2"/></svg>
    <div class="abs" style="left:18px;top:150px;font-weight:700;font-size:11px;color:#3a2a00;text-decoration:underline">Advanced Search</div>
  </div>
</section>

<!-- keep in touch -->
<section class="abs side light" style="top:556px;height:175px;border-color:#ccc">
  <h3>Keep <b style="color:#fff">in</b> <b>Touch</b></h3>
  <div class="body" style="position:relative;height:139px">
    <div class="abs" style="left:12px;top:9px;width:200px;line-height:15px;color:#222">Newsletter with Deals &amp; Local Knowledge To Your Inbox</div>
    <div class="abs" style="left:8px;top:53px;font-weight:700;color:#333;font-size:11px">username :</div>
    <div class="abs field" style="left:79px;top:50px;width:146px"></div>
    <div class="abs" style="left:8px;top:83px;font-weight:700;color:#333;font-size:11px">password :</div>
    <div class="abs field" style="left:79px;top:80px;width:146px"></div>
    <div class="abs" style="left:13px;top:113px;display:flex;align-items:center;gap:5px;color:var(--blue-deep);font-size:11px"><span style="width:18px;height:18px;background:#3b5998;display:inline-block"></span>Social page</div>
    <div class="abs round" style="left:173px;top:106px;width:46px;height:25px;border-radius:12px;background:linear-gradient(#3db4f2,var(--blue-deep));color:#fff;font-size:15px;text-align:center;line-height:25px">Go</div>
  </div>
</section>

<!-- deals -->
<section class="abs side" style="top:748px;height:190px">
  <h3>Dea<b>ls</b></h3>
  <div style="position:relative;height:152px">
    <div class="abs" role="img" aria-label="Promotional image of a hand holding a small house" style="left:8px;top:8px;width:100px;height:78px;background:linear-gradient(#2f6fb0,#b8cde0 60%,#e6c9a3);border:2px solid #fff"></div>
    <div class="abs" style="left:117px;top:8px;width:112px;line-height:16px;color:#222">Lorem ipsum dolor sit amet, consectetuer adipiscing elit. Nam nibh.a</div>
    <div class="abs" style="left:36px;top:94px;font-size:12px;color:#3a2a00">$XXX</div>
    <div class="abs" style="left:14px;top:122px;width:80px;height:24px;background:#fff;border:1px solid #ccc;font-size:12px;color:#333;line-height:22px;text-align:center;letter-spacing:.5px">View more..</div>
    <div class="abs" role="img" aria-label="Illustration of discount coupons in an envelope" style="left:150px;top:86px;width:75px;height:62px;background:linear-gradient(#7fc94a,#3a95d6 50%,#e8e8e8);border-radius:6px"></div>
  </div>
</section>

<!-- welcome -->
<div class="abs" role="img" aria-label="Illustration of city buildings" style="left:320px;top:331px;width:54px;height:54px;background:linear-gradient(135deg,#8fc0e0,#4a7fa8 60%,#6b9a45);border-radius:4px"></div>
<div class="abs round" style="left:386px;top:334px;font-size:21px;color:var(--gold-deep);letter-spacing:1px">Welcome to</div>
<div class="abs" style="left:386px;top:356px;font:700 23px 'Josefin Sans',Arial,sans-serif;color:#333;letter-spacing:.5px">Tui Crib &amp; Seaside Cottages</div>
<div class="abs" style="left:386px;top:388px;width:260px;border-top:1px dashed #ccc"></div>
<div class="abs round" style="left:910px;top:323px;width:76px;height:33px;border-radius:16px;background:linear-gradient(#3fb7f5,var(--blue-deep));color:#fff;font-size:15px;text-align:center;line-height:33px;box-shadow:1px 2px 3px #999">Help</div>

<div class="abs intro" style="left:329px;top:396px;width:620px">
  <p class="lead">Lorem ipsum dolor sit amet, consectetuer adipiscing elit. Nam nibh. Nunc varius facilisis eros. Sed erat. In in velit quis arcu ornare laoreet. <span>Curabitur adipiscing luctus massa. Integer ut purus ac augue commodo commodo. Nunc nec mi eu justo tempor consectetuer. Etiam vitae nisl. In dignissim lacus ut ante. Cras elit lectus, bibendum a, adipiscing vitae, commodo et, dui. Ut tincidunt tortor. Donec nonummy, enim in lacinia pulvinar,</span></p>
  <p style="margin-top:17px">velit tellus scelerisque augue, ac posuere libero urna eget neque. Cras ipsum. Vestibulum pretium, lectus nec venenatis volutpat, purus lectus ultrices risus, a condimentum risus mi et quam. velit tellus scelerisque augue, ac posuere libero urna eget neque. Cras ipsum. Vestibulum pretium, lectus nec venenatis volutpat, purus lectus ultrices risus, a condimentum risus mi et quam. velit tellus scelerisque augue, ac posuere libero urna eget neque. Cras ipsum. Vestibulum pretium, lectus nec venenatis volutpat, purus lectus ultrices risus, a condimentum risus mi et quam.</p>
</div>

<div class="abs banner">Just can’t find what you’re looking for? Contact us for a<br><em>personal property search.</em></div>

<div class="abs feature" style="left:344px;background:var(--dark)">
  <div class="photo" role="img" aria-label="Photo of a weatherboard family home with a white picket fence, captioned What are you looking for?" style="background:linear-gradient(#9ec6e6,#e0c7a0 45%,#c9a985 65%,#4f8a3a)"></div>
  <h4 style="color:#fff">Browse <span style="color:var(--gold)">Homes</span></h4>
  <p style="color:#ccc">Lorem ipsum dolor sit amet, consectetuer adipiscing elit. Nam nibh.a</p>
</div>
<div class="abs feature" style="left:663px;background:var(--gold)">
  <div class="photo" role="img" aria-label="Photo of a resort pool with a thatched umbrella and palm trees by the sea" style="background:linear-gradient(#4ea0e6,#bfe2f5 45%,#6aa4b8 60%,#2f8fc8 80%,#1f6fa8)"></div>
  <h4 style="color:#222">Local <span style="color:#fff">Knowledge</span></h4>
  <p style="color:#333">Lorem ipsum dolor sit amet, consectetuer adipiscing elit. Nam nibh.a</p>
</div>

<footer class="abs footer">
  <h5 class="abs" style="left:67px;top:17px">Featured Works</h5>
  <p class="abs" style="left:67px;top:48px;width:690px;line-height:17.5px;font-size:10.3px;color:var(--gold);font-weight:700">Lorem ipsum dolor sit amet, consectetuer adipiscing elit. Nam nibh. Nunc varius facilisis eros. Sed erat. In in velit quis arcu ornare laoreet. <span class="soft" style="font-weight:400">Curabitur adipiscing luctus massa. Integer ut purus ac augue commodo commodo. Nunc nec mi eu justo tempor consectetuer. Etiam vitae nisl. In dignissim lacus ut ante. Cras elit lectus, bibendum a, adipiscing vitae, commodo et, dui. Ut tincidunt tortor. Donec nonummy, enim in lacinia pulvinar,</span></p>
  <div class="abs round" style="left:67px;top:141px;font-size:17px;color:#fff">Follow Us on :</div>
  <div class="abs" style="left:180px;top:138px;width:99px;height:26px;background:#fff;border:1px solid #999;font-size:11px;color:#333;line-height:24px;padding-left:24px">You like this.</div>
  <div class="abs social" style="left:64px;top:170px;width:307px;height:44px;background:#2b2b2b;border:1px solid #444">
    <i style="left:4px;background:#e8861d"></i><i style="left:49px;background:#3b5998"></i><i style="left:95px;background:#33a7dc"></i><i style="left:140px;background:#f07a16"></i><i style="left:185px;background:#3a9a3a"></i>
    <span style="position:absolute;left:232px;top:14px;color:#fff;font-size:12px">Share page</span>
  </div>
  <h5 class="abs" style="left:814px;top:17px">Contact us</h5>
  <div class="abs" style="left:814px;top:56px;color:#fff;font-size:11.5px;line-height:17.5px">Firm: Pohutu Ltd<br>Address: 48 Dune Road,<br>Marram Sands 3120<br>Phone: +64 7 555 0142<br>Fax: +64 7 555 0143<br>Email: stay@tuicribcottages.co.nz</div>
  <div class="abs fnav" style="left:426px;top:215px"><span>Home</span><span>About us</span><span>List Your Home</span><span>LocalKnowledge</span><span>Browse Homes</span><span>Packages</span></div>
</footer>

</body>
</html>
```